Packaging for Hair Fibers Product

We are a start up company looking for a new packaging design for hair building fibers. These are aimed at predominantly men but also women as well. We already have a logo and i have the packaging design from our competitors. We are wanting to keep the look masculine as 90% of our users will be middle aged men. We would like the colours to be black and white but are open to other colours as well.
It will need to have our logo and the following somewhere on the front.
"Instant Fuller & Thicker Hair" & "Natural Hair Building Fibers" "28g" or "Net Weight 28g"
We only need the front of the packaging designed, please make the other sides of the packaging the same colour but blank.
Target Market(s)
Men 25+
Industry/Entity Type
Hair And Beauty
Requirements
Must have
- Logo which i have included. and the following somewhere on the front.
- "Instant Fuller & Thicker Hair" ; "Natural Hair Building Fibers" "28g" or "Net Weight 28g"
Nice to have
- Make it stand out from the competition or similar to the brantiq example.

```html
<!DOCTYPE html>
<html lang="en">
<head>
<meta charset="utf-8">
<title>Fibrelux Hair Fibers – Carton Dieline</title>
<link rel="stylesheet" href="https://fonts.googleapis.com/css2?family=Open+Sans:wght@400;600&display=swap">
<style>
  :root {
    --paper: #ffffff;
    --carton: #2a2828;
    --band: #6b7d9a;
    --cut-line: #b0206a;
    --ink-light: #ffffff;
    --ink-soft: #d8d8d8;
  }
  html, body {
    margin: 0;
    padding: 0;
    width: 1200px;
    height: 1200px;
    overflow: hidden;
    background: var(--paper);
  }
  .canvas {
    width: 1200px;
    height: 1200px;
    display: block;
  }
  .panel { fill: var(--carton); stroke: var(--cut-line); stroke-width: 0.9; stroke-linejoin: round; }
  .fold { stroke: var(--cut-line); stroke-width: 0.7; fill: none; }
  .accent-band { fill: var(--band); }
  .brand-name {
    font-family: "Open Sans", sans-serif;
    font-weight: 400;
    font-size: 19px;
    letter-spacing: 3px;
    fill: var(--ink-light);
  }
  .headline-instant {
    font-family: "Open Sans", sans-serif;
    font-weight: 400;
    font-size: 27px;
    letter-spacing: 1.5px;
    fill: var(--ink-light);
  }
  .headline-sub {
    font-family: "Open Sans", sans-serif;
    font-weight: 400;
    font-size: 9.5px;
    letter-spacing: 2.4px;
    fill: var(--ink-light);
  }
  .headline-hair {
    font-family: "Open Sans", sans-serif;
    font-weight: 400;
    font-size: 54px;
    fill: var(--ink-light);
  }
  .tagline {
    font-family: "Open Sans", sans-serif;
    font-weight: 400;
    font-size: 8.6px;
    fill: var(--ink-soft);
  }
  .net-weight {
    font-family: "Open Sans", sans-serif;
    font-weight: 400;
    font-size: 10px;
    fill: var(--ink-soft);
  }
</style>
</head>
<body>
<svg class="canvas" viewBox="10 200 730 700" preserveAspectRatio="xMidYMid meet" xmlns="http://www.w3.org/2000/svg" aria-label="Flat carton dieline for Fibrelux hair building fibers">

  <!-- top closure -->
  <g class="top-flaps">
    <path class="panel" d="M199 438 L199 245 Q199 235 209 235 L347 235 Q357 235 357 245 L357 438 Z"/>
    <line class="fold" x1="199" y1="280" x2="357" y2="280"/>
    <path class="panel" d="M40 438 L40 410 L55 402 L55 357 Q55 347 67 347 L185 347 L185 410 L199 420 L199 438 Z"/>
    <path class="panel" d="M357 438 L357 420 L372 410 L372 347 L488 347 Q500 347 500 357 L500 402 L516 410 L516 438 Z"/>
  </g>

  <!-- bottom closure -->
  <g class="bottom-flaps">
    <path class="panel" d="M40 730 L199 730 L199 748 L120 770 L120 805 L40 805 Z"/>
    <path class="panel" d="M199 730 L357 730 L357 855 L313 855 L313 805 L240 805 L240 855 L199 855 Z"/>
    <path class="panel" d="M357 730 L516 730 L516 805 L435 805 L435 770 L357 748 Z"/>
    <path class="panel" d="M516 730 L673 730 L673 745 L628 805 L628 855 L560 855 L560 805 L516 745 Z"/>
  </g>

  <!-- body panels -->
  <g class="body-panels">
    <rect class="panel side-panel" x="40" y="438" width="159" height="292"/>
    <rect class="panel front-panel" x="199" y="438" width="158" height="292"/>
    <rect class="panel side-panel" x="357" y="438" width="159" height="292"/>
    <rect class="panel back-panel" x="516" y="438" width="157" height="292"/>
    <path class="panel glue-flap" d="M673 438 L710 446 L710 722 L673 730 Z"/>
    <rect class="accent-band" x="40" y="450" width="633" height="12"/>
    <line class="fold" x1="199" y1="438" x2="199" y2="730"/>
    <line class="fold" x1="357" y1="438" x2="357" y2="730"/>
    <line class="fold" x1="516" y1="438" x2="516" y2="730"/>
    <line class="fold" x1="673" y1="438" x2="673" y2="730"/>
  </g>

  <!-- front panel artwork -->
  <g class="front-artwork">
    <text class="brand-name" x="278" y="492" text-anchor="middle">FIBRELUX</text>
    <text class="headline-instant" x="276" y="583" text-anchor="middle">INSTANT</text>
    <text class="headline-sub" x="276" y="597" text-anchor="middle">FULLER &amp; THICKER</text>
    <text class="headline-hair" x="276" y="640" text-anchor="middle">HAIR</text>
    <text class="tagline" x="276" y="652" text-anchor="middle">Natural Hair Building Fibers</text>
    <text class="net-weight" x="278" y="720" text-anchor="middle">28g</text>
  </g>
</svg>
</body>
</html>
```